Past Gold Rivers Oz Tour Flyer

I need a dynamic flyer for a concert tour.
I have uploaded the file. Please use these ingredients for the design.
The font for the title is Jellyka Jellyfish lower case from www.glyphoria-loft.com
We are getting close!! We just need bright colours, the headings to STAND OUT and Byron Bay has to be moved to under NSW Bellingen.
Thanks for all your hard work!
We are targeting a wide range of customers from old age to children and families
Tour

```html
<!DOCTYPE html>
<html lang="en">
<head>
<meta charset="utf-8">
<title>Past Gold Rivers Oz Tour Flyer</title>
<link href="https://fonts.googleapis.com/css2?family=Reenie+Beanie&family=Source+Sans+3:wght@400;600;700;800&display=swap" rel="stylesheet">
<style>
  :root{
    --page:#ffffff;
    --teal:rgba(18,108,124,0.86);
    --ink:#111418;
    --navy:#1e2190;
    --yellow:#f6e63a;
    --swoosh-yellow:rgba(246,226,58,0.8);
    --pink:#e0336e;
    --white:#ffffff;
    --photo-top:#3a2414;
    --photo-mid:#8a4a1c;
    --photo-warm:#e2861e;
    --photo-low:#c24a22;
  }
  html,body{margin:0;width:1200px;height:1000px;overflow:hidden;background:var(--page);}
  .flyer{position:absolute;left:310px;top:72px;width:595px;height:842px;overflow:hidden;
    font-family:"Source Sans 3",Arial,sans-serif;color:var(--white);}
  .stage-photo{position:absolute;inset:0;
    background:
      radial-gradient(ellipse 45% 40% at 62% 55%, var(--photo-warm) 0%, rgba(226,134,30,0) 70%),
      radial-gradient(ellipse 60% 30% at 40% 85%, var(--photo-low) 0%, rgba(194,74,34,0) 75%),
      linear-gradient(180deg,var(--photo-top) 0%,var(--photo-mid) 45%,#b8661f 75%,#9c3a1c 100%);}
  .title-band{position:absolute;left:36px;top:0;width:219px;height:842px;background:var(--teal);}
  .swooshes{position:absolute;inset:0;}
  .tour-title{position:absolute;left:50px;top:40px;width:200px;margin:0;
    font-family:"Reenie Beanie",cursive;font-weight:400;color:var(--white);line-height:0.78;}
  .tour-title .w1{display:block;font-size:46px;padding-left:8px;}
  .tour-title .w2{display:block;font-size:64px;}
  .tour-title .w3{display:block;font-size:60px;padding-left:30px;}
  .dots{position:absolute;left:36px;width:219px;top:188px;text-align:center;font-size:0;}
  .dots span{display:inline-block;width:4px;height:4px;border-radius:50%;background:var(--pink);margin:0 1px;}
  .choir-name{position:absolute;left:36px;width:219px;top:214px;margin:0;text-align:center;
    font-size:15px;font-weight:600;color:var(--ink);letter-spacing:-0.2px;}
  .tour-sub{position:absolute;left:36px;width:219px;top:236px;text-align:center;
    font-family:"Reenie Beanie",cursive;font-size:19px;color:var(--yellow);}
  .region{position:absolute;margin:0;}
  .region h3{margin:0;font-size:12px;font-weight:800;color:var(--navy);letter-spacing:0.3px;}
  .region ul{list-style:none;margin:2px 0 0 12px;padding:0;font-size:10px;line-height:12.2px;
    text-shadow:0 0 2px rgba(120,60,10,0.55);}
  .vic{left:69px;top:576px;}
  .act{left:172px;top:664px;}
  .nsw{left:282px;top:694px;}
  .nsw .cols{display:flex;gap:14px;}
  .nsw .cols ul:last-child{margin-top:14px;}
  .qld{left:484px;top:755px;}
  .tickets{position:absolute;right:33px;top:586px;text-align:right;font-size:10px;line-height:12.5px;}
  .tickets h3{margin:0 0 2px;font-size:12px;font-weight:800;color:var(--yellow);}
  .tickets .phone{margin-left:10px;}
  .partner{position:absolute;top:775px;height:60px;background:#000;display:flex;align-items:center;
    justify-content:center;font-size:10px;font-weight:600;color:var(--white);text-align:center;}
  .partner-choir{left:52px;width:108px;}
  .partner-ember{left:173px;width:67px;}
</style>
</head>
<body>
<main class="flyer">
  <div class="stage-photo" role="img" aria-label="Photo of a smiling young dancer in a bright orange and yellow outfit and headband, performing on stage with a grass skirt, other choir members behind"></div>

  <div class="title-band"></div>

  <svg class="swooshes" viewBox="0 0 595 842" aria-hidden="true">
    <path d="M0,268 C150,262 330,300 595,360 L595,366 C330,308 150,270 0,276 Z" fill="rgba(224,51,110,0.45)"/>
    <path d="M470,420 C520,405 560,402 595,398 L595,404 C560,408 520,412 470,426 Z" fill="rgba(244,228,58,0.75)"/>
    <path d="M340,652 C430,600 520,565 595,545 L595,610 C520,632 430,650 340,652 Z" fill="rgba(224,51,110,0.78)"/>
    <path d="M255,462 C100,505 15,600 38,690 C65,800 250,842 420,842 L595,842 L595,740 C450,710 300,650 225,600 C160,555 190,500 255,462 Z" fill="var(--swoosh-yellow)"/>
  </svg>

  <h1 class="tour-title"><span class="w1">past</span><span class="w2">gold</span><span class="w3">rivers</span></h1>
  <div class="dots"><span></span><span></span><span></span></div>
  <h2 class="choir-name">The Riverlight Children’s Choir</h2>
  <div class="tour-sub">Australia Tour</div>

  <section class="region vic"><h3>VICTORIA</h3>
    <ul><li>Geelong</li><li>Sunbury</li><li>Melbourne</li><li>Bendigo</li><li>Albury</li></ul></section>
  <section class="region act"><h3>A.C.T.</h3><ul><li>Canberra</li></ul></section>
  <section class="region nsw"><h3>N.S.W.</h3>
    <div class="cols">
      <ul><li>Nowra</li><li>Sydney</li><li>Wollongong</li><li>Blue Mountains</li></ul>
      <ul><li>Port Macquarie</li><li>Laurieton</li><li>Taree</li><li>Bellingen</li><li>Byron Bay</li></ul>
    </div></section>
  <section class="region qld"><h3>QLD</h3><ul><li>Gold Coast</li><li>Sunshine Coast</li></ul></section>

  <section class="tickets"><h3>TICKETS &amp; INFO</h3>
    <div>www.embervoices.org</div>
    <div>Contact Lena Hartwell<span class="phone">0412 587309</span></div></section>

  <div class="partner partner-choir">Riverlight Choir</div>
  <div class="partner partner-ember">Ember Voices</div>
</main>
</body>
</html>
```